Property Investor needs business card

Hi, we need a business card/logo/email footer/letterhead for a small family property investment business (based in Australia), to just give things a bit more of a professional "look".
Saying that, the property manager is in his late 30s, and is a fun, interesting guy so it doesn't have to be too "corporate" and serious.
Going with eg an 8cmx4cm card size could also make it a bit more interesting. Colour-wise - am relaxed.
Also, the property isn't so much "residential" ie houses/apartments, more "commercial" ie factories, office buildings, shops - in case that helps?
Lastly, the business name is "QHT", so you could also try to do something with those letters.
Enjoy!

```html
<!DOCTYPE html>
<html lang="en">
<head>
<meta charset="utf-8">
<title>QHT Property Investments – Business Cards</title>
<link rel="stylesheet" href="https://fonts.googleapis.com/css2?family=Cabin:wght@400;700&display=swap">
<style>
  :root {
    --canvas: #ffffff;
    --frame: #e4e4e4;
    --ink-light: #ffffff;
    --ink-soft: #cfcfcf;

    --mint-sky: #aef0bf;
    --mint-house: #55bb98;
    --violet-sky: #a2a8fd;
    --violet-house: #444cfe;
    --sage-sky: #5f7f72;
    --plum-house: #6e5a86;
    --rose-sky: #f36284;
    --teal-house: #215b6e;
  }
  * { margin: 0; padding: 0; box-sizing: border-box; }
  html, body {
    width: 1200px; height: 940px; overflow: hidden;
    background: var(--canvas);
  }
  .sheet {
    position: relative; width: 1200px; height: 940px;
    font-family: "Cabin", sans-serif;
  }
  .card {
    position: absolute; width: 290px; height: 460px; display: block;
  }
  .col-1 { left: 4px; } .col-2 { left: 304px; } .col-3 { left: 600px; } .col-4 { left: 896px; }
  .row-1 { top: 2px; } .row-2 { top: 466px; }

  .house { stroke: var(--frame); stroke-width: 3; stroke-linejoin: miter; }
  .rule { stroke: var(--ink-soft); stroke-width: 0.8; }

  .brand-mark { fill: var(--ink-soft); font-family: "Cabin", sans-serif; font-weight: 400; font-size: 34px; letter-spacing: 2px; }
  .brand-tag { fill: var(--ink-soft); font-family: "Cabin", sans-serif; font-weight: 700; font-size: 8.5px; }
  .contact { fill: var(--ink-light); font-family: "Cabin", sans-serif; font-weight: 400; font-size: 7.6px; }
  .brand-mark-small { fill: var(--ink-soft); font-family: "Cabin", sans-serif; font-weight: 400; font-size: 11px; letter-spacing: 1px; }
  .brand-tag-small { fill: var(--ink-soft); font-family: "Cabin", sans-serif; font-weight: 700; font-size: 3px; }

  .mint .sky { fill: var(--mint-sky); } .mint .house { fill: var(--mint-house); }
  .violet .sky { fill: var(--violet-sky); } .violet .house { fill: var(--violet-house); }
  .plum .sky { fill: var(--sage-sky); } .plum .house { fill: var(--plum-house); }
  .teal .sky { fill: var(--rose-sky); } .teal .house { fill: var(--teal-house); }
</style>
</head>
<body>
<main class="sheet">

  <svg class="card card-front mint col-1 row-1" viewBox="0 0 145 230" aria-label="QHT card front, mint">
    <rect class="sky" x="0" y="0" width="144" height="108"/>
    <polygon class="house" points="2,110 30,110 90,72 143,107 143,228 2,228"/>
    <text class="brand-mark" x="72" y="165" text-anchor="middle">QHT</text>
    <line class="rule" x1="18" y1="185" x2="132" y2="185"/>
    <text class="brand-tag" x="74" y="197" text-anchor="middle">Property Investments</text>
  </svg>

  <svg class="card card-back mint col-2 row-1" viewBox="0 0 145 230" aria-label="QHT card back, mint">
    <rect class="sky" x="0" y="0" width="144" height="104"/>
    <polygon class="house" points="2,110 30,110 60,74 90,74 143,104 143,228 2,228"/>
    <line class="rule" x1="10" y1="138" x2="134" y2="138"/>
    <text class="contact" x="72" y="155" text-anchor="middle">Name</text>
    <text class="contact" x="72" y="167" text-anchor="middle">555 0192 736</text>
    <text class="contact" x="72" y="179" text-anchor="middle">qht@qhtmail.com</text>
    <line class="rule" x1="10" y1="192" x2="134" y2="192"/>
    <text class="brand-mark-small" x="72" y="211" text-anchor="middle">QHT</text>
    <text class="brand-tag-small" x="72" y="216" text-anchor="middle">Property Investments</text>
  </svg>

  <svg class="card card-front violet col-3 row-1" viewBox="0 0 145 230" aria-label="QHT card front, violet">
    <rect class="sky" x="0" y="0" width="144" height="108"/>
    <polygon class="house" points="2,110 30,110 90,72 143,107 143,228 2,228"/>
    <text class="brand-mark" x="72" y="165" text-anchor="middle">QHT</text>
    <line class="rule" x1="18" y1="185" x2="132" y2="185"/>
    <text class="brand-tag" x="74" y="197" text-anchor="middle">Property Investments</text>
  </svg>

  <svg class="card card-back violet col-4 row-1" viewBox="0 0 145 230" aria-label="QHT card back, violet">
    <rect class="sky" x="0" y="0" width="144" height="104"/>
    <polygon class="house" points="2,110 30,110 60,74 90,74 143,104 143,228 2,228"/>
    <line class="rule" x1="10" y1="138" x2="134" y2="138"/>
    <text class="contact" x="72" y="155" text-anchor="middle">Name</text>
    <text class="contact" x="72" y="167" text-anchor="middle">555 0192 736</text>
    <text class="contact" x="72" y="179" text-anchor="middle">qht@qhtmail.com</text>
    <line class="rule" x1="10" y1="192" x2="134" y2="192"/>
    <text class="brand-mark-small" x="72" y="211" text-anchor="middle">QHT</text>
    <text class="brand-tag-small" x="72" y="216" text-anchor="middle">Property Investments</text>
  </svg>

  <svg class="card card-front plum col-1 row-2" viewBox="0 0 145 230" aria-label="QHT card front, plum">
    <rect class="sky" x="0" y="0" width="144" height="108"/>
    <polygon class="house" points="2,110 30,110 90,72 143,107 143,228 2,228"/>
    <text class="brand-mark" x="72" y="165" text-anchor="middle">QHT</text>
    <line class="rule" x1="18" y1="185" x2="132" y2="185"/>
    <text class="brand-tag" x="74" y="197" text-anchor="middle">Property Investments</text>
  </svg>

  <svg class="card card-back plum col-2 row-2" viewBox="0 0 145 230" aria-label="QHT card back, plum">
    <rect class="sky" x="0" y="0" width="144" height="104"/>
    <polygon class="house" points="2,110 30,110 60,74 90,74 143,104 143,228 2,228"/>
    <line class="rule" x1="10" y1="138" x2="134" y2="138"/>
    <text class="contact" x="72" y="155" text-anchor="middle">Name</text>
    <text class="contact" x="72" y="167" text-anchor="middle">555 0192 736</text>
    <text class="contact" x="72" y="179" text-anchor="middle">qht@qhtmail.com</text>
    <line class="rule" x1="10" y1="192" x2="134" y2="192"/>
    <text class="brand-mark-small" x="72" y="211" text-anchor="middle">QHT</text>
    <text class="brand-tag-small" x="72" y="216" text-anchor="middle">Property Investments</text>
  </svg>

  <svg class="card card-front teal col-3 row-2" viewBox="0 0 145 230" aria-label="QHT card front, teal">
    <rect class="sky" x="0" y="0" width="144" height="108"/>
    <polygon class="house" points="2,110 30,110 90,72 143,107 143,228 2,228"/>
    <text class="brand-mark" x="72" y="165" text-anchor="middle">QHT</text>
    <line class="rule" x1="18" y1="185" x2="132" y2="185"/>
    <text class="brand-tag" x="74" y="197" text-anchor="middle">Property Investments</text>
  </svg>

  <svg class="card card-back teal col-4 row-2" viewBox="0 0 145 230" aria-label="QHT card back, teal">
    <rect class="sky" x="0" y="0" width="144" height="104"/>
    <polygon class="house" points="2,110 30,110 60,74 90,74 143,104 143,228 2,228"/>
    <line class="rule" x1="10" y1="138" x2="134" y2="138"/>
    <text class="contact" x="72" y="155" text-anchor="middle">Name</text>
    <text class="contact" x="72" y="167" text-anchor="middle">555 0192 736</text>
    <text class="contact" x="72" y="179" text-anchor="middle">qht@qhtmail.com</text>
    <line class="rule" x1="10" y1="192" x2="134" y2="192"/>
    <text class="brand-mark-small" x="72" y="211" text-anchor="middle">QHT</text>
    <text class="brand-tag-small" x="72" y="216" text-anchor="middle">Property Investments</text>
  </svg>

</main>
</body>
</html>
```